" Incluímos agricultores familiares na cadeia de valor agropecuárias de empresa e cooperativas com viabilidade e sustentabilidade. O nosso foco è resiliência climática do produtur "

```html
<!DOCTYPE html>
<html lang="pt-BR">
<head>
<meta charset="UTF-8">
<title>Campo Vivo – Envelope</title>
<link rel="stylesheet" href="https://fonts.googleapis.com/css2?family=Montserrat:wght@400;600;800&display=swap">
<style>
  :root {
    --bg: #ece8e2;
    --paper: #ffffff;
    --flap-back: #f4f4f4;
    --brand-blue: #1f3f93;
    --brand-orange: #f2a516;
    --faint-blue: #dfe5f2;
    --faint-orange: #fbecc8;
    --text-grey: #6b6b6b;
  }
  html, body {
    margin: 0;
    width: 1200px;
    height: 1200px;
    overflow: hidden;
    background: var(--bg);
    font-family: "Montserrat", sans-serif;
  }
  .stage { position: relative; width: 1200px; height: 1200px; }
  .envelope {
    position: absolute;
    top: 204px;
    width: 490px;
    height: 810px;
    background: var(--paper);
    border-radius: 10px 10px 2px 2px;
    box-shadow: 0 4px 14px rgba(0,0,0,0.12);
    overflow: hidden;
  }
  .envelope--front { left: 108px; }
  .envelope--back { left: 614px; }
  .flap { position: absolute; left: 0; top: 0; width: 100%; height: 48px; }
  .envelope--front .flap { background: var(--brand-blue); }
  .envelope--back .flap { background: var(--flap-back); border-bottom: 1px solid #e2e2e2; }

  .brand {
    position: absolute; left: 0; right: 0; top: 400px;
    display: flex; align-items: center; justify-content: center; gap: 12px;
  }
  .brand__dot { width: 40px; height: 40px; border-radius: 50%; background: var(--brand-orange); }
  .brand__name { font-weight: 800; font-size: 42px; color: var(--brand-blue); letter-spacing: 1px; }

  .swoosh { position: absolute; left: 0; bottom: 0; width: 100%; height: 120px; }

  .accent-bar {
    position: absolute; left: 0; top: 690px; width: 6px; height: 96px; background: var(--brand-blue);
  }
  .contact {
    position: absolute; left: 18px; top: 610px; list-style: none; margin: 0; padding: 0;
    font-size: 8.5px; color: var(--text-grey); line-height: 1.3;
  }
  .contact li { display: flex; align-items: flex-start; gap: 8px; margin-bottom: 14px; }
  .contact__icon { width: 11px; height: 11px; border-radius: 50%; background: var(--brand-orange); flex: none; }

  .watermark {
    position: absolute; right: 22px; bottom: 70px;
    display: flex; align-items: center; gap: 10px;
  }
  .watermark__dot { width: 30px; height: 30px; border-radius: 50%; background: var(--faint-orange); }
  .watermark__name { font-weight: 800; font-size: 30px; color: var(--faint-blue); letter-spacing: 1px; }
</style>
</head>
<body>
<main class="stage">
  <section class="envelope envelope--front">
    <div class="flap"></div>
    <div class="brand">
      <span class="brand__dot"></span>
      <span class="brand__name">CAMPO VIVO</span>
    </div>
    <svg class="swoosh" viewBox="0 0 490 120" preserveAspectRatio="none">
      <path d="M0 120 L0 95 C120 40 300 30 490 40 L490 70 C300 55 150 70 0 120 Z" fill="var(--brand-blue)"/>
      <path d="M0 80 C140 30 320 20 490 25" stroke="var(--brand-blue)" stroke-width="2" fill="none"/>
    </svg>
  </section>

  <section class="envelope envelope--back">
    <div class="flap"></div>
    <span class="accent-bar"></span>
    <ul class="contact">
      <li><span class="contact__icon"></span><span>(00) 0000-0000</span></li>
      <li><span class="contact__icon"></span><span>campovivo.com.br<br>contato@campovivo.com.br</span></li>
      <li><span class="contact__icon"></span><span>agro.campovivo.com.br<br>rede@campovivo.com.br</span></li>
      <li><span class="contact__icon"></span><span>Rua das Flores, 100 - Centro<br>Cidade - UF - CEP 00000-000</span></li>
    </ul>
    <div class="watermark">
      <span class="watermark__dot"></span>
      <span class="watermark__name">CAMPO VIVO</span>
    </div>
  </section>
</main>
</body>
</html>
```